farvinta labs cybersecurity website design and development

website design and development for a cybersecurity company. we have a logo and would like site to suit logo colors and look
cybersecurity website should be secure and look professional
main example of site we want to use: https://www.plomvex.example/
site should be usable on tablet and phones

For each design proposal, please could you provide details of what language you'll use to code the website.

Target Market(s)

insurance companies, financial institutions, private SME, Africa and Europe

Coding

Coded - Design and coding required

Number of Pages Required

5+ page

Requirements
Must have
• 9 Pages:
Home
About us
Contacts
Partners
Blog
Services
( consulting, vulnerability assessment, information systems security audit, ISO compliance, Penetration testing, security awareness training, social engineering test, protection against DDoS, procurement )
Resources
Technologies
Careers
Nice to have
• nice to have all services have their own pages.
design based on logo colors and look

please provide what will be use to code the website

```html
<!DOCTYPE html>
<html lang="en">
<head>
<meta charset="utf-8">
<title>Farvinta Labs – Cybersecure your business</title>
<link rel="stylesheet" href="https://fonts.googleapis.com/css2?family=Montserrat:ital,wght@0,300;0,400;0,500;0,600;0,700;0,800;1,500&family=Roboto:wght@400;500&display=swap">
<style>
:root{
  --navy:#0d1a5c;
  --navy-deep:#0a1340;
  --royal:#1a3a9e;
  --blue:#0d4ba8;
  --bright:#1f5fd0;
  --accent:#1e3c9a;
  --ink:#141414;
  --grey:#666b78;
  --pale:#f3f5fb;
  --white:#ffffff;
  --line:#c9ceda;
}
*{box-sizing:border-box;margin:0;padding:0}
html,body{width:1200px;height:2980px;overflow:hidden}
body{position:relative;background:var(--white);font-family:'Montserrat',sans-serif;color:var(--ink)}
.abs{position:absolute}

/* header / hero */
.hero{left:0;top:0;width:1200px;height:600px;background:radial-gradient(ellipse at 35% 45%,#1d3596 0%,#13257a 40%,var(--navy-deep) 100%)}
.hero-photo{left:660px;top:0;width:540px;height:575px;background:linear-gradient(120deg,#0f2a8a 0%,#1b5ad6 45%,#2f8cf0 70%,#0f2d86 100%);opacity:.9}
.brand{display:flex;align-items:center;gap:10px}
.brand-mark{width:62px;height:62px;border-radius:50%;background:var(--white);border:5px solid #2c56c6}
.brand-name{font-family:'Montserrat',sans-serif;font-weight:700;font-size:25px;color:var(--white);line-height:1}
.brand-tag{display:block;font-size:7px;font-weight:700;letter-spacing:.3px;margin-top:3px;color:var(--white)}
.site-nav{display:flex;align-items:center;gap:26px;font-family:'Roboto',sans-serif;font-size:15px;color:var(--white)}
.site-nav .home{width:17px;height:15px}
.hero-title{left:100px;top:205px;font-size:67px;font-weight:700;color:var(--white);letter-spacing:-.5px}
.hero-lede{left:101px;top:285px;font-size:18.5px;line-height:27px;color:var(--white);font-weight:400;white-space:nowrap}
.btn-primary{display:inline-block;background:linear-gradient(180deg,#1d55c4,#0f3d9e);color:var(--white);font-family:'Roboto',sans-serif;font-weight:500;font-size:15px;text-align:center}
.hero-btn{left:100px;top:357px;width:152px;height:44px;line-height:44px}

/* partner strip */
.partners{left:0;top:574px;width:1200px;height:148px;background:var(--pale);border-top-left-radius:170px 120px}
.partner-row{left:150px;top:634px;width:900px;display:flex;justify-content:space-between;align-items:center}
.partner{font-family:'Montserrat',sans-serif;font-weight:700;font-size:22px;color:#7d828c}
.partner.dark{color:#202020}
.circle-arrow{width:38px;height:38px;border-radius:50%;background:var(--white);border:1.5px solid var(--line);display:flex;align-items:center;justify-content:center}
.circle-arrow.blue{border-color:#3659c9}

/* section titles */
.section-title{left:0;width:1200px;text-align:center;font-size:38px;font-weight:300;letter-spacing:.5px;color:var(--ink)}
.section-title b{font-weight:800}
.divider{left:525px;width:150px;height:30px}

/* services */
.service{top:915px;width:235px;height:308px;background:linear-gradient(160deg,#2c3f9c 0%,#1f2f8c 60%,#1a2a80 100%);color:var(--white);text-align:center;clip-path:polygon(0 0,100% 0,100% 100%,14px 100%,0 calc(100% - 14px))}
.service.active{background:linear-gradient(160deg,#1659c4 0%,#0e47ae 100%)}
.service-icon{position:absolute;left:0;width:100%;display:flex;justify-content:center}
.service-name{position:absolute;left:0;width:100%;font-size:15.5px;font-weight:500;letter-spacing:.2px;line-height:21px}
.service-bar{position:absolute;left:50%;width:32px;height:2px;margin-left:-16px;background:var(--white)}
.service-copy{position:absolute;left:12px;width:211px;top:148px;font-size:11.5px;line-height:20px}

/* welcome */
.welcome{left:0;top:1232px;width:1200px;height:488px;background:var(--pale);clip-path:polygon(0 0,100% 0,100% 100%,100px 100%,0 360px)}
.welcome-photo{left:168px;top:1295px;width:322px;height:336px;background:linear-gradient(150deg,#cfd6e4 0%,#8da0c8 45%,#2f5bc2 75%,#1c2f7a 100%)}
.kicker{left:600px;top:1308px;font-size:22px;font-weight:400;color:var(--accent);letter-spacing:.3px}
.welcome-title{left:599px;top:1332px;font-size:37px;font-weight:800;color:var(--ink)}
.welcome-copy{left:600px;top:1420px;width:430px;font-size:13px;line-height:22.5px;color:var(--grey)}
.btn-light{left:600px;top:1594px;width:154px;height:44px;line-height:44px;background:var(--white);color:var(--blue);font-family:'Roboto',sans-serif;font-weight:500;font-size:15px;text-align:center;box-shadow:0 3px 10px rgba(20,40,100,.08)}

/* testimonials */
.review{top:1950px;width:320px;height:272px;background:var(--white);box-shadow:0 6px 18px rgba(30,40,80,.08);text-align:center;clip-path:polygon(0 0,100% 0,100% 100%,14px 100%,0 calc(100% - 14px))}
.review-top{position:absolute;top:0;left:0;width:100%;height:2px;background:#d4d7de}
.review.featured .review-top{background:var(--accent)}
.avatar{top:1915px;width:72px;height:72px;border-radius:50%;background:linear-gradient(180deg,#e6e8ec,#c4c8d0);border:3px solid var(--white);box-shadow:0 2px 6px rgba(0,0,0,.12)}
.review-name{position:absolute;top:58px;left:0;width:100%;font-size:17px;font-weight:600;color:var(--ink)}
.review.featured .review-name{color:var(--accent)}
.review-role{position:absolute;top:82px;left:0;width:100%;font-size:12px;color:var(--grey)}
.review-quote{position:absolute;top:107px;left:18px;width:284px;font-size:13px;line-height:22.5px;font-style:italic;font-weight:500;color:#222}
.quote-mark{top:2205px;width:60px;height:40px;text-align:center;font-family:Georgia,serif;font-size:80px;line-height:80px;font-weight:700;color:#c5c8cf}
.quote-mark.featured{color:var(--accent)}

/* careers */
.careers{left:0;top:2330px;width:1200px;height:400px;background:linear-gradient(180deg,#1153ad 0%,#123d93 55%,#0f2a6e 100%)}
.careers .section-title{color:var(--white)}
.field{height:45px;background:var(--white);font-size:13px;color:#6a6f7a;padding-left:16px;line-height:45px;clip-path:polygon(0 0,100% 0,100% 100%,10px 100%,0 calc(100% - 10px))}
.btn-submit{left:524px;top:2614px;width:152px;height:44px;line-height:44px;background:var(--white);color:var(--blue);font-family:'Roboto',sans-serif;font-weight:500;font-size:15px;text-align:center;clip-path:polygon(0 0,100% 0,100% 100%,10px 100%,0 calc(100% - 10px))}
.to-top{left:1114px;top:2597px;width:62px;height:62px;border-radius:50%;background:var(--bright);border:3px solid var(--white);display:flex;align-items:center;justify-content:center}

/* footer */
.footer{left:0;top:2728px;width:1200px;height:252px;background:linear-gradient(180deg,#0c1650,#0a1038)}
.footer-rule{left:100px;top:2882px;width:1000px;height:1px;background:#3a4379}
.copyright{left:100px;top:2920px;font-size:14px;color:var(--white)}
.social{top:2910px;width:36px;height:36px;border:1.5px solid #8a92bf;display:flex;align-items:center;justify-content:center}
.social span{width:8px;height:8px;border-radius:50%;background:var(--white)}
</style>
</head>
<body>

<!-- Hero -->
<div class="abs hero"></div>
<div class="abs hero-photo" role="img" aria-label="Two IT specialists walking through a glowing blue server room"></div>

<header class="abs brand" style="left:100px;top:13px">
  <div class="brand-mark"></div>
  <div class="brand-name">Farvinta Labs<span class="brand-tag">CYBERSECURE YOUR BUSINESS</span></div>
</header>
<nav class="abs site-nav" style="left:381px;top:36px">
  <svg class="home" viewBox="0 0 17 15"><path d="M8.5 0 L17 7.5 H14.5 V15 H10.5 V10 H6.5 V15 H2.5 V7.5 H0 Z" fill="#3b7de8"/></svg>
  <span>About us</span><span>Contacts</span><span>Partners</span><span>Blog</span><span>Services</span><span>Resources</span><span>Technologies</span><span>Careers</span>
</nav>

<h1 class="abs hero-title">Farvinta Labs</h1>
<p class="abs hero-lede">Lorem ipsum dolor met, consectetur adipcing<br>elit, sed do eiusmod</p>
<a class="abs btn-primary hero-btn">GET STARTED</a>

<!-- Partners -->
<div class="abs partners"></div>
<div class="abs circle-arrow" style="left:56px;top:634px"><svg width="16" height="10" viewBox="0 0 16 10"><path d="M15 5 H2 M6 1 L2 5 L6 9" stroke="#555" stroke-width="1.6" fill="none"/></svg></div>
<div class="abs partner-row">
  <span class="partner">Ridgeline</span>
  <span class="partner">Mailbrook</span>
  <span class="partner" style="font-weight:500">your logo</span>
  <span class="partner dark">dummy.</span>
  <span class="partner">Harlow</span>
  <span class="partner" style="font-weight:800">DUMMY</span>
</div>
<div class="abs circle-arrow blue" style="left:1099px;top:634px"><svg width="16" height="10" viewBox="0 0 16 10"><path d="M1 5 H14 M10 1 L14 5 L10 9" stroke="#1a3a9e" stroke-width="2" fill="none"/></svg></div>

<!-- Services -->
<h2 class="abs section-title" style="top:805px">OUR <b>SERVICES</b></h2>
<svg class="abs divider" style="top:860px" viewBox="0 0 150 30"><path d="M0 15 H62 M88 15 H150" stroke="#1a3a9e" stroke-width="1.5"/><circle cx="75" cy="15" r="11" fill="#2c56c6"/></svg>

<div class="abs service" style="left:0">
  <div class="service-icon" style="top:100px"><svg width="50" height="52" viewBox="0 0 50 52" fill="none" stroke="#fff" stroke-width="2"><rect x="8" y="4" width="34" height="26"/><path d="M4 30 H46 L40 46 H10 Z M25 46 V52"/></svg></div>
  <div class="service-name" style="top:178px">CONSULTING</div>
  <div class="service-bar" style="top:202px"></div>
</div>
<div class="abs service" style="left:241px">
  <div class="service-icon" style="top:100px"><svg width="48" height="56" viewBox="0 0 48 56" fill="none" stroke="#fff" stroke-width="2"><rect x="4" y="6" width="36" height="48"/><rect x="14" y="1" width="16" height="8"/><path d="M10 20 l3 3 5-5 M22 21 H34 M10 32 l3 3 5-5 M22 33 H34 M10 44 l3 3 5-5 M22 45 H30"/></svg></div>
  <div class="service-name" style="top:178px">ISO COMPLIANCE</div>
  <div class="service-bar" style="top:202px"></div>
</div>
<div class="abs service active" style="left:483px">
  <div class="service-icon" style="top:34px"><svg width="56" height="52" viewBox="0 0 56 52" fill="none" stroke="#fff" stroke-width="2"><path d="M24 2 L40 8 V20 Q40 32 24 38 Q8 32 8 20 V8 Z"/><rect x="12" y="36" width="28" height="14"/><path d="M12 43 H40 M20 36 V43 M30 43 V50 M44 2 L52 10 M52 2 V10 H44"/><circle cx="24" cy="18" r="4"/></svg></div>
  <div class="service-name" style="top:105px">PENETRATION TESTING</div>
  <div class="service-bar" style="top:134px"></div>
  <p class="service-copy">Lorem ipsum dolt amet, conseetur adipiscg elit, sed do eimod tempor incididunt ut laboredolore magna aliqua. Quis ipsum spendisse ultrices gravida. Risus</p>
  <svg style="position:absolute;left:108px;top:268px" width="18" height="10" viewBox="0 0 18 10"><path d="M0 5 H16 M12 1 L16 5 L12 9" stroke="#fff" stroke-width="2" fill="none"/></svg>
</div>
<div class="abs service" style="left:724px">
  <div class="service-icon" style="top:104px"><svg width="48" height="52" viewBox="0 0 48 52" fill="none" stroke="#fff" stroke-width="2"><path d="M24 2 L44 9 V24 Q44 40 24 50 Q4 40 4 24 V9 Z"/><rect x="16" y="22" width="16" height="13"/><path d="M19 22 V17 Q24 11 29 17 V22"/></svg></div>
  <div class="service-name" style="top:178px">SECURITY AWARENESS<br>TRAINING</div>
  <div class="service-bar" style="top:222px"></div>
</div>
<div class="abs service" style="left:966px">
  <div class="service-icon" style="top:100px"><svg width="54" height="52" viewBox="0 0 54 52" fill="none" stroke="#fff" stroke-width="2"><rect x="14" y="20" width="26" height="30"/><circle cx="27" cy="35" r="8"/><path d="M25 31 L31 35 L25 39 Z"/><rect x="20" y="2" width="14" height="10"/><circle cx="8" cy="12" r="5"/><circle cx="46" cy="12" r="5"/></svg></div>
  <div class="service-name" style="top:178px">SOCIAL ENGINEERING TEST</div>
  <div class="service-bar" style="top:202px"></div>
</div>

<!-- Welcome -->
<div class="abs welcome"></div>
<div class="abs welcome-photo" role="img" aria-label="Two colleagues reviewing work on a laptop"></div>
<div class="abs kicker">WELCOME TO</div>
<h2 class="abs welcome-title">FARVINTA LABS</h2>
<svg class="abs" style="left:600px;top:1376px" width="100" height="28" viewBox="0 0 100 28"><circle cx="14" cy="14" r="11" fill="#2c56c6"/><path d="M34 14 H96" stroke="#1a3a9e" stroke-width="1.5"/></svg>
<p class="abs welcome-copy">Lorem ipsum dolor sit amet, consectetur adipiscing elo eiusmod tempor incididunt ut labore et dolore magna aliqua. Quis ipsum suspendisse ultmaecenas accumsan lacus vel facilisis. Lom dolor sit amet, consectetur adipiscing elo eiusmod tempor incididunt ut labore et dolore magna aliqua. Quis um suspendisse ultrices gravida. Risus commodo viverra maecenas accumsan lacus vel ultmaecenas accumsan lacus facilisis.</p>
<a class="abs btn-light">GET STARTED</a>

<!-- Testimonials -->
<h2 class="abs section-title" style="top:1802px">CLIENT <b>TESTIMONIALS</b></h2>
<svg class="abs divider" style="top:1857px" viewBox="0 0 150 30"><path d="M0 15 H62 M88 15 H150" stroke="#1a3a9e" stroke-width="1.5"/><circle cx="75" cy="15" r="11" fill="#2c56c6"/></svg>

<div class="abs circle-arrow" style="left:42px;top:2078px"><svg width="16" height="10" viewBox="0 0 16 10"><path d="M15 5 H2 M6 1 L2 5 L6 9" stroke="#555" stroke-width="1.6" fill="none"/></svg></div>

<div class="abs review" style="left:100px"><div class="review-top"></div>
  <div class="review-name">John Doe</div><div class="review-role">Sed ut perspiciatis</div>
  <p class="review-quote">“Lorem ipsum dolr sit amet, consectetur adipiscing elit, semod tempor incididunt ut labore et dolore magna aliqua. Quis ipsum suspendisse ultrices gravida. Risus commodo viverra maecenas accumsan lacus vel facilisis. ”</p>
</div>
<div class="abs review featured" style="left:440px"><div class="review-top"></div>
  <div class="review-name">John Doe</div><div class="review-role">Sed ut perspiciatis</div>
  <p class="review-quote">“Lorem ipsum dolr sit amet, consectetur adipiscing elit, semod tempor incididunt ut labore et dolore magna aliqua. Quis ipsum suspendisse ultrices gravida. Risus commodo viverra maecenas accumsan lacus vel facilisis. ”</p>
</div>
<div class="abs review" style="left:780px"><div class="review-top"></div>
  <div class="review-name">John Doe</div><div class="review-role">Sed ut perspiciatis</div>
  <p class="review-quote">“Lorem ipsum dolr sit amet, consectetur adipiscing elit, semod tempor incididunt ut labore et dolore magna aliqua. Quis ipsum suspendisse ultrices gravida. Risus commodo viverra maecenas accumsan lacus vel facilisis. ”</p>
</div>
<div class="abs avatar" style="left:224px" role="img" aria-label="Client portrait"></div>
<div class="abs avatar" style="left:564px" role="img" aria-label="Client portrait"></div>
<div class="abs avatar" style="left:904px" role="img" aria-label="Client portrait"></div>
<div class="abs quote-mark" style="left:230px">”</div>
<div class="abs quote-mark featured" style="left:570px">”</div>
<div class="abs quote-mark" style="left:910px">”</div>

<div class="abs circle-arrow blue" style="left:1118px;top:2078px"><svg width="16" height="10" viewBox="0 0 16 10"><path d="M1 5 H14 M10 1 L14 5 L10 9" stroke="#1a3a9e" stroke-width="2" fill="none"/></svg></div>

<!-- Careers -->
<section class="abs careers">
  <h2 class="abs section-title" style="top:68px">CAREERS <b>SERVICE QUOTE</b></h2>
</section>
<svg class="abs" style="left:540px;top:2452px" width="120" height="30" viewBox="0 0 120 30"><path d="M0 15 H42 M78 15 H120" stroke="#fff" stroke-width="1.5"/><circle cx="60" cy="15" r="11" fill="#fff"/><circle cx="60" cy="15" r="7" fill="#2c56c6"/></svg>
<svg class="abs" style="left:0;top:2330px" width="1200" height="400" viewBox="0 0 1200 400"><path d="M1200 80 Q1185 330 1060 395 L0 395 L0 400 L1200 400 Z" fill="#0c1650"/><path d="M1200 80 Q1185 330 1060 395 L0 395" stroke="#fff" stroke-width="5" fill="none"/></svg>

<div class="abs field" style="left:222px;top:2497px;width:248px">Frist Name</div>
<div class="abs field" style="left:476px;top:2497px;width:248px">Last Name</div>
<div class="abs field" style="left:730px;top:2497px;width:248px">Email</div>
<div class="abs field" style="left:222px;top:2548px;width:248px">Phone</div>
<div class="abs field" style="left:476px;top:2548px;width:248px">Company Name</div>
<div class="abs field" style="left:730px;top:2548px;width:248px">upload Resume
  <svg style="position:absolute;right:12px;top:16px" width="12" height="12" viewBox="0 0 12 12"><path d="M6 1 L2 5 H4.5 V8 H7.5 V5 H10 Z M1 10 H11 V12 H1 Z" fill="#555"/></svg>
</div>
<a class="abs btn-submit">SUBMIT NOW</a>
<div class="abs to-top"><svg width="14" height="28" viewBox="0 0 14 28"><path d="M7 27 V3 M1 9 L7 2 L13 9" stroke="#fff" stroke-width="3" fill="none"/></svg></div>

<!-- Footer -->
<footer class="abs footer"></footer>
<div class="abs brand" style="left:100px;top:2780px">
  <div class="brand-mark"></div>
  <div class="brand-name" style="color:#2c56c6">Farvinta Labs<span class="brand-tag" style="color:#fff">CYBERSECURE YOUR BUSINESS</span></div>
</div>
<nav class="abs site-nav" style="left:381px;top:2806px">
  <svg class="home" viewBox="0 0 17 15"><path d="M8.5 0 L17 7.5 H14.5 V15 H10.5 V10 H6.5 V15 H2.5 V7.5 H0 Z" fill="#3b7de8"/></svg>
  <span>About us</span><span>Contacts</span><span>Partners</span><span>Blog</span><span>Services</span><span>Resources</span><span>Technologies</span><span>Careers</span>
</nav>
<div class="abs footer-rule"></div>
<p class="abs copyright">Copyright 2021 Farvinta Labs. All Rights Reserved</p>
<a class="abs social" style="left:971px" aria-label="Social profile 1"><span></span></a>
<a class="abs social" style="left:1014px" aria-label="Social profile 2"><span></span></a>
<a class="abs social" style="left:1058px" aria-label="Social profile 3"><span></span></a>

</body>
</html>
```